Stylish High End Wedding Videography/Films Website (BMTS)

We need a modern and high-end website look for our wedding video and films business. We films weddings all over the United Kingdom and at European destinations so need something to reflect our work. The website should be visually stunning with images and videos being the focal point as this is what our services are;

I have uploads of some items I like and the features the site needs to have. These have been taken from other websites using standout features.

We need the following pages;

1 - Homepage
2 - Films Index Page
3 - Individual Films Page
4 - Prices / Collection Page
5 - Reviews
6 - Options
7 - About
8 - Contact
9 - Blog Index
10 - Blog Page

All pages must be consistent so have a similar style.

Pages on menu:
Films
Prices
Reviews
Options
About
Contact

We require a responsive look too. Over 90% of our visitors access the website via their mobile devices.

Please use the colours from our logo to incorporate into the website.

Target Market(s)

Wedding Couples

Industry/Entity Type

Wedding Photography

Number of Pages Required

5+ page

Font styles to use
Sans Serif
Script

Requirements
Must have
• The logo must be in the centre of the menu at the top.

Social icons at the bottom of the page.

Use only two fonts including Lore which is supplied
Nice to have
• Different video for each page on the top header. This will play behind the menu.

```html
<!DOCTYPE html>
<html lang="en">
<head>
<meta charset="utf-8">
<title>BMTS Wedding Films</title>
<link rel="stylesheet" href="https://fonts.googleapis.com/css2?family=Raleway:wght@300;400;500&family=Yellowtail&display=swap">
<style>
:root{
  --gold:#a98a4f;
  --ink:#2a2522;
  --muted:#9a9592;
  --line:#e6e1dc;
  --grey-band:#f7f7f7;
  --cream:#fdf5ef;
  --white:#ffffff;
  --hero-dark:#2b1d14;
  --sans:'Raleway',sans-serif;
  --script:'Yellowtail',cursive;
}
*{margin:0;padding:0;box-sizing:border-box}
html,body{width:1200px;height:4181px;overflow:hidden;background:var(--white)}
body{position:relative;font-family:var(--sans);color:var(--ink)}
.abs{position:absolute}
.photo{position:absolute;overflow:hidden}

/* hero */
.hero{left:0;top:0;width:1200px;height:706px;background:radial-gradient(ellipse at 45% 35%,#a57a4a 0%,#6a4a2e 35%,#3a281b 70%,#1f1510 100%)}
.topbar{left:106px;top:18px;width:988px;height:22px;border-bottom:1px solid rgba(255,255,255,.25);color:#e8ddd0;font-size:11px;letter-spacing:.5px}
.topbar .follow{position:absolute;left:0;top:3px}
.topbar .dot{position:absolute;top:0;width:16px;height:16px;border:1.5px solid #e8ddd0;border-radius:50%}
.topbar .rsvp{position:absolute;right:70px;top:4px}
.nav{left:0;top:100px;width:1200px;color:#fff;font-size:12px;letter-spacing:.3px}
.nav span{position:absolute;top:2px}
.brand-top{left:500px;top:80px;width:200px;text-align:center;color:#fff}
.brand-name{font-family:var(--sans);font-weight:500;letter-spacing:4px}
.play{left:546px;top:268px;width:108px;height:108px;border:3px solid #fff;border-radius:50%}
.hero-title{left:0;top:410px;width:1200px;text-align:center;font-family:var(--script);font-size:76px;color:#fff}
.hero-sub{left:0;top:541px;width:1200px;text-align:center;color:#fff;font-size:17px;letter-spacing:5px;font-weight:300}
.hero-sub i{display:inline-block;width:60px;height:1px;background:rgba(255,255,255,.6);vertical-align:middle;margin:0 26px}

/* intro */
.intro-title{left:0;top:822px;width:1200px;text-align:center;font-family:var(--script);font-size:48px;line-height:56px;color:var(--ink)}
.divider{left:325px;top:980px;width:560px;height:1px;background:var(--line)}
.divider-mark{left:584px;top:962px;width:36px;height:36px}
.intro-text{left:280px;top:1030px;width:640px;text-align:center;font-size:13px;line-height:26px;color:var(--muted);font-weight:300}

.grid-cap{color:#fff;text-align:center;font-size:16px;letter-spacing:2px}
.grid-cap small{display:block;font-size:10px;letter-spacing:1.5px;margin-top:6px}
.zoom{width:38px;height:38px;border-radius:50%;background:#fff;margin:0 auto 16px;position:relative}

/* funky */
.band-grey{left:0;top:1749px;width:1200px;height:636px;background:var(--grey-band)}
.funky-title{left:129px;top:1985px;font-size:37px;line-height:47px;letter-spacing:1.5px;font-weight:300}
.funky-text{left:131px;top:2108px;width:410px;font-size:12.5px;line-height:26px;color:var(--muted);font-weight:300}
.video-cap{color:#fff;font-weight:300}

/* testimonial */
.quote{left:135px;top:2470px;width:740px;font-family:var(--script);font-size:28px;line-height:37px;color:#fff}
.thanks{left:135px;top:2650px;font-family:var(--script);font-size:28px;color:#fff}
.who{left:137px;top:2752px;color:#fff;font-size:19px;letter-spacing:.5px;font-weight:300}
.where{left:137px;top:2785px;color:#fff;font-size:11.5px;letter-spacing:.5px}
.arrows{font-size:20px;font-weight:300}

/* services */
.band-cream{left:0;top:2888px;width:1200px;height:544px;background:var(--cream)}
.card{top:2861px;width:452px;height:457px;background:var(--white);box-shadow:0 2px 10px rgba(0,0,0,.03);padding:60px 52px 0}
.card h3{font-size:37px;line-height:47px;font-weight:300;letter-spacing:1px}
.card p{font-size:12.5px;line-height:26px;color:var(--muted);font-weight:300;margin-top:26px}
.card h3+p{margin-top:42px}
.card .ico{position:absolute;right:30px;top:30px}

/* mark */
.big-mark{left:0;top:3520px;width:1200px;text-align:center;font-size:96px;letter-spacing:10px;color:var(--gold);font-weight:500}

/* footer */
.foot-line{top:4036px;height:1px;background:var(--line)}
.foot-brand{left:500px;top:4018px;width:200px;text-align:center}
.foot-contact{left:173px;top:4096px;font-size:12.5px;line-height:22px;color:var(--ink)}
.copy{left:0;top:4109px;width:1200px;text-align:center;font-size:12.5px}
.social{top:4103px;width:24px;height:24px;border:2px solid var(--ink);border-radius:50%}
</style>
</head>
<body>

<!-- HERO -->
<div class="photo hero" role="img" aria-label="Close-up of a bride and groom kissing, warm golden light"></div>
<div class="abs topbar">
  <span class="follow">FOLLOW US ON:</span>
  <span class="dot" style="left:111px"></span>
  <span class="dot" style="left:139px"></span>
  <span class="dot" style="left:167px"></span>
  <span class="rsvp">RSVP</span>
  <svg class="abs" style="right:32px;top:0" width="18" height="18" viewBox="0 0 18 18" fill="none" stroke="#e8ddd0" stroke-width="1.3"><path d="M3 6h12l-1 10H4z"/><path d="M6 6V4a3 3 0 0 1 6 0v2"/></svg>
  <svg class="abs" style="right:2px;top:0" width="18" height="18" viewBox="0 0 18 18" fill="none" stroke="#e8ddd0" stroke-width="1.4"><circle cx="7.5" cy="7.5" r="5.5"/><path d="M11.5 11.5l5 5"/></svg>
</div>
<nav class="abs nav">
  <span style="left:171px">FILMS</span>
  <span style="left:286px">PRICES</span>
  <span style="left:406px">OPTIONS</span>
  <span style="left:723px">REVIEWS</span>
  <span style="left:856px">ABOUT</span>
  <span style="left:980px">CONTACT</span>
</nav>
<div class="abs brand-top">
  <div class="brand-name" style="font-size:22px">BMTS</div>
  <div style="font-size:7px;letter-spacing:3px;margin-top:3px">WEDDING FILMS</div>
</div>
<div class="abs play">
  <svg class="abs" style="left:36px;top:28px" width="40" height="48" viewBox="0 0 40 48" fill="none" stroke="#fff" stroke-width="3"><path d="M4 3l32 21L4 45z"/></svg>
</div>
<div class="abs hero-title">Oliver &amp; Rose</div>
<div class="abs hero-sub"><i></i>WEDDING&nbsp; VIDEOGRAPHY<i></i></div>

<!-- INTRO -->
<h1 class="abs intro-title">Bram Mallory is a wedding filmmaker based<br>in the North East of England.</h1>
<div class="abs divider"></div>
<svg class="abs divider-mark" viewBox="0 0 36 36"><rect x="10" y="10" width="16" height="16" fill="none" stroke="var(--gold)" stroke-width="2" transform="rotate(45 18 18)"/></svg>
<p class="abs intro-text">We film weddings in a fun and natural way. All weddings are totally unique to the couple. If you are looking for a wedding film for your special day we'd love to hear from you.</p>

<div class="photo" style="left:127px;top:1158px;width:233px;height:216px;background:linear-gradient(135deg,#d9d2c6,#4a4a52)" role="img" aria-label="Bride with bouquet beside groom in navy suit"></div>
<div class="photo" style="left:367px;top:1158px;width:232px;height:216px;background:linear-gradient(135deg,#6f7a78,#2e3440)" role="img" aria-label="Groom embracing bride in lace veil"></div>
<div class="photo" style="left:606px;top:1158px;width:233px;height:216px;background:linear-gradient(160deg,#6d5a3c,#4b3c26)" role="img" aria-label="Couple in front of an Italian church">
  <div class="abs grid-cap" style="left:0;top:70px;width:233px"><div class="zoom"><svg class="abs" style="left:11px;top:11px" width="16" height="16" viewBox="0 0 16 16" fill="none" stroke="#333" stroke-width="1.5"><circle cx="6.5" cy="6.5" r="4.5"/><path d="M10 10l4.5 4.5"/></svg></div>LENA + MARCO<small>ITALY WEDDING</small></div>
</div>
<div class="photo" style="left:845px;top:1158px;width:232px;height:216px;background:linear-gradient(135deg,#c26a2e,#e9e2da)" role="img" aria-label="Couple kissing against autumn leaves"></div>
<div class="photo" style="left:127px;top:1382px;width:233px;height:215px;background:linear-gradient(135deg,#b58e6a,#e7ddd0)" role="img" aria-label="Groom kissing bride at reception"></div>
<div class="photo" style="left:367px;top:1382px;width:232px;height:215px;background:linear-gradient(135deg,#8f8f8c,#d8d4cf)" role="img" aria-label="Couple walking along a city bridge"></div>
<div class="photo" style="left:606px;top:1382px;width:233px;height:215px;background:linear-gradient(135deg,#4a3a30,#c69c7c)" role="img" aria-label="Close-up of couple smiling together"></div>
<div class="photo" style="left:845px;top:1382px;width:232px;height:215px;background:linear-gradient(135deg,#c9c1a6,#2c3d6b)" role="img" aria-label="Bride hugging laughing groom with bouquet"></div>

<!-- FUNKY -->
<div class="abs band-grey"></div>
<svg class="abs" style="left:134px;top:1925px" width="40" height="36" viewBox="0 0 40 36"><rect x="12" y="8" width="18" height="18" fill="none" stroke="var(--gold)" stroke-width="2.5" transform="rotate(45 21 17)"/></svg>
<h2 class="abs funky-title">PREFER SOMETHING A<br>BIT MORE FUNKY?</h2>
<p class="abs funky-text">If you are a couple who prefers something a bit different to the styles above then why not go for our alternative option.</p>
<div class="photo" style="left:588px;top:1889px;width:489px;height:326px;background:linear-gradient(135deg,#5d7a3a,#c9b29a 60%,#6d6a4a)" role="img" aria-label="Bride smelling her bouquet outdoors">
  <div class="abs" style="left:208px;top:126px;width:74px;height:74px;border:2.5px solid #fff;border-radius:50%"><svg class="abs" style="left:25px;top:19px" width="28" height="34" viewBox="0 0 28 34" fill="none" stroke="#fff" stroke-width="2.5"><path d="M3 2l22 15L3 32z"/></svg></div>
  <div class="abs video-cap" style="left:32px;top:268px;font-size:19px">TOM HADLEY</div>
  <div class="abs video-cap" style="left:32px;top:295px;font-size:12px;letter-spacing:1.5px">28.04.1990</div>
  <div class="abs video-cap" style="left:408px;top:286px;font-size:19px;border-left:1px solid rgba(255,255,255,.6);padding-left:6px">12:05</div>
</div>

<!-- TESTIMONIAL -->
<div class="photo" style="left:0;top:2386px;width:1200px;height:503px;background:linear-gradient(90deg,#4f7a2a 0%,#7fae48 35%,#9cc26a 55%,#8a9a6a 68%,#1c1c22 80%,#e9dcd2 100%)" role="img" aria-label="Groom and bride holding a pink and white bouquet against green foliage"></div>
<blockquote class="abs quote">One of the best decisions we made was choosing you guys to film our wedding! It's absolutely fantastic, it has everyone so emotional watching it, we can't thank you enough for capturing our special day! You were amazing from start to finish.</blockquote>
<div class="abs thanks">Thanks so much.</div>
<div class="abs who">HANNAH AND JOEL</div>
<div class="abs where">WILLOW BARN HEXLEY</div>
<div class="abs arrows" style="left:582px;top:2806px;color:#fff">‹&nbsp;&nbsp;&nbsp;›</div>

<!-- SERVICES -->
<div class="abs band-cream"></div>
<div class="abs card" style="left:135px">
  <svg class="ico" width="52" height="62" viewBox="0 0 52 62" fill="none" stroke="#e2e2e2" stroke-width="2"><rect x="4" y="22" width="44" height="36"/><path d="M4 22l40-12 3 9"/><path d="M12 30h28M12 38h28M12 46h20"/></svg>
  <h3>CINEMATIC<br>HIGHLIGHTS FILM</h3>
  <p>A highlights film, a harmony of moving imagery, vocals and music, which is unique to you.</p>
  <p>I coentrate on the emotion of the day and the people who are important to you.</p>
  <p>This cinematic highlights film is a memory that you will watch for the rest of your lives. This film will outlive lives and generations.</p>
</div>
<div class="abs card" style="left:617px">
  <svg class="ico" width="46" height="70" viewBox="0 0 46 70" fill="none" stroke="#e2e2e2" stroke-width="2.5"><rect x="12" y="3" width="22" height="38" rx="11"/><path d="M4 30a19 19 0 0 0 38 0M23 49v14M13 65h20"/></svg>
  <h3>CEREMONY AND<br>SPEECHES</h3>
  <p>Want to hear the moment you say your vows or I Do or even see your first kiss? We film the ceremony in its entirety.</p>
  <p>We also film the entire speeches and toasts so you can relive all those sincere and fun moments.</p>
  <p>We provide you with a separate edit with multiple camera angles.</p>
</div>
<div class="abs arrows" style="left:582px;top:3342px;color:var(--ink)">‹&nbsp;&nbsp;&nbsp;›</div>

<!-- MARK -->
<div class="abs big-mark">BMTS</div>

<div class="photo" style="left:0;top:3714px;width:237px;height:241px;background:linear-gradient(135deg,#5a4032,#d8b79a)" role="img" aria-label="Couple with flower crown touching foreheads"></div>
<div class="photo" style="left:240px;top:3714px;width:237px;height:241px;background:linear-gradient(135deg,#dcdcdc,#2f3a5a)" role="img" aria-label="Bride under veil kissing groom"></div>
<div class="photo" style="left:480px;top:3714px;width:238px;height:241px;background:linear-gradient(160deg,#5f4a32,#3d2f20)" role="img" aria-label="Couple at an Italian wedding">
  <div class="abs" style="left:101px;top:80px;width:36px;height:36px;border-radius:50%;background:#fff"></div>
  <div class="abs grid-cap" style="left:0;top:132px;width:238px">LENA + MARCO<small>ITALY WEDDING</small></div>
</div>
<div class="photo" style="left:721px;top:3714px;width:237px;height:241px;background:linear-gradient(135deg,#2e4a2a,#d9cfc4)" role="img" aria-label="Groom kissing bride among roses"></div>
<div class="photo" style="left:961px;top:3714px;width:239px;height:241px;background:linear-gradient(135deg,#c9a07a,#2a2a2e)" role="img" aria-label="Smiling couple cheek to cheek"></div>

<!-- FOOTER -->
<div class="abs foot-line" style="left:100px;width:400px"></div>
<div class="abs foot-line" style="left:700px;width:400px"></div>
<div class="abs foot-brand">
  <div class="brand-name" style="font-size:20px;color:var(--gold)">BMTS</div>
  <div style="font-size:7px;letter-spacing:3px;margin-top:3px;color:var(--gold)">WEDDING FILMS</div>
</div>
<div class="abs foot-contact">07000 123 456<br>hello@bmtsfilms.example</div>
<div class="abs copy">Copyright © 2020 Bram Mallory</div>
<div class="abs social" style="left:880px"></div>
<div class="abs social" style="left:914px"></div>
<div class="abs social" style="left:949px"></div>

</body>
</html>
```